I have a PHP web application to manage IT support calls and require a front-end design and user logon screen.

I have attached the current design which needs improving.

I have 2 current designs. The 2nd design is one I have been working on but requires a "professional touch". I also require the tables designed with dummy data from the 1st design.

I have attached my company logo in AI format which I would like incorporated into the design. There should also be a placeholder to supply the users company name upon login.

The screenshots I have attached should explain what I am looking for.

The Home Page should include charts which show statistical information such as:
Number of support tickets logged per month. Bar Chart etc.
Number of currently open support tickets.
Number of Quote Requests awaiting a response.
Number of Files and file repository.
Number of Reports.
Number of Customers.

For the Jobs and Customers pages the table fields should be designed as per the attached screenshots but a better looking tables. The table options such as uploading a file and adding a customer - these options can be changed and displayed differently.

Quotes page should display quotes returned and a "request a quote form".

Files page should have a good structure for browsing through an archive of files.

Profile page should have the option to include a profile picture.

An additional side page should be created for a web based calendar (these calendar entries will be updated by code).

The navbar should also include an alerts section.
The current attached design I have is based on bootstraps navbar.

Inspiration: http://plenvaro.com/freebie/free-admin-templates-for-backend-panels/

Hopefully this above link will show you some navigation style designs that I am looking for.

Please note, I will be doing the PHP coding myself and it is just the page designs I require in either HTML and or PHP format. I also require the CSS files for this project.
I need the code in a format where I can add and remove items in the menu from the code and not PSD/image based format.

If you think this project requires a higher budget let me know what you would expect and I will increase it!

Any questions, please let me know.
Dummy data can be shown for design purposes.

I have provided you a dummy login to our current system to show you the system:
https://reef.vomilbrixtonsolutions.co.uk/
username: dan.hollow@vomilbrixtonsolutions.co.uk
password:K#72zqTm

```html
<!DOCTYPE html>
<html lang="en">
<head>
<meta charset="utf-8">
<title>REEF | Viewing Job</title>
<link rel="stylesheet" href="https://fonts.googleapis.com/css2?family=Open+Sans:wght@300;400;600&display=swap">
<style>
  :root {
    --blue: #2393ec;
    --blue-dark: #1f86d8;
    --sidebar: #25272f;
    --sidebar-line: #17181d;
    --sidebar-line-light: #33353e;
    --sidebar-text: #d9dbe0;
    --page-bg: #f0f0f0;
    --panel-bg: #ffffff;
    --panel-border: #dedede;
    --row-line: #e6e6e6;
    --text: #222222;
    --text-soft: #555555;
    --table-head: #e8e8e8;
    --link-red: #e8211f;
    --white: #ffffff;
  }
  * { box-sizing: border-box; margin: 0; padding: 0; }
  html, body { width: 1200px; height: 963px; overflow: hidden; }
  body {
    position: relative;
    background: var(--page-bg);
    font-family: "Open Sans", Arial, sans-serif;
    color: var(--text);
  }

  /* Top bar */
  .topbar {
    position: absolute; left: 0; top: 0; width: 1200px; height: 56px;
    background: var(--blue); color: var(--white);
  }
  .brand { position: absolute; left: 31px; top: 9px; font-size: 30px; font-weight: 300; line-height: 38px; }
  .brand-divider { position: absolute; left: 136px; top: 12px; width: 1px; height: 32px; background: var(--white); }
  .brand-tagline { position: absolute; left: 153px; top: 14px; font-size: 24px; font-weight: 300; line-height: 32px; }
  .user-menu { position: absolute; left: 936px; top: 18px; font-size: 17px; line-height: 22px; }
  .user-menu .caret { display: inline-block; margin-left: 12px; border-left: 4px solid transparent; border-right: 4px solid transparent; border-top: 5px solid var(--white); vertical-align: 3px; }
  .help-link { position: absolute; left: 1138px; top: 18px; font-size: 17px; line-height: 22px; }

  /* Sidebar */
  .sidebar {
    position: absolute; left: 0; top: 56px; width: 215px; height: 907px;
    background: var(--sidebar);
  }
  .sidebar-logo {
    height: 136px; display: flex; align-items: center; justify-content: center; gap: 10px;
    border-bottom: 1px solid var(--sidebar-line);
  }
  .sidebar-logo .mark { width: 22px; height: 22px; border-radius: 50%; background: var(--white); }
  .sidebar-logo .name { color: var(--white); font-size: 20px; font-weight: 600; letter-spacing: 0.5px; line-height: 1.15; }
  .nav { list-style: none; }
  .nav-item {
    position: relative; height: 53.7px; display: flex; align-items: center;
    padding-left: 55px; font-size: 14px; color: var(--sidebar-text);
    border-top: 1px solid var(--sidebar-line-light); border-bottom: 1px solid var(--sidebar-line);
  }
  .nav-item svg { position: absolute; left: 19px; top: 50%; transform: translateY(-50%); fill: var(--sidebar-text); }
  .nav-item.is-active::before { content: ""; position: absolute; left: 0; top: 0; bottom: 0; width: 5px; background: var(--blue); }

  /* Page heading */
  .page-head {
    position: absolute; left: 215px; top: 56px; width: 985px; height: 69px; background: var(--white);
  }
  .page-head h1 { position: absolute; left: 25px; top: 17px; font-size: 30px; font-weight: 300; line-height: 40px; color: var(--text); }

  /* Panels */
  .panel {
    position: absolute; left: 240px; width: 929px;
    background: var(--panel-bg); border: 1px solid var(--panel-border);
  }
  .panel-title {
    height: 46px; background: var(--blue); color: var(--white);
    font-size: 24px; font-weight: 300; line-height: 46px; padding-left: 14px; margin: -1px -1px 0;
  }
  .panel-personal { top: 157px; height: 160px; }
  .panel-job { top: 345px; height: 253px; }
  .panel-tabs { top: 631px; height: 259px; }

  .info-row { position: absolute; left: 17px; width: 885px; border-bottom: 1px solid var(--row-line); }
  .info-row:last-child { border-bottom: none; }
  .field { position: absolute; font-size: 16px; line-height: 24px; }
  .field .label { position: absolute; right: 0; font-weight: 600; white-space: nowrap; }
  .field .label::after { content: ":"; position: absolute; left: calc(100% + 9px); font-weight: 600; }
  .value { position: absolute; font-size: 16px; line-height: 24px; color: var(--text-soft); white-space: nowrap; }
  .value.wrap { white-space: normal; width: 756px; text-align: justify; }

  /* Tabs */
  .tab-bar { position: absolute; left: 24px; top: 10px; width: 881px; height: 58px; border: 1px solid var(--panel-border); }
  .tab { position: absolute; top: 0; height: 56px; display: flex; align-items: center; gap: 8px; font-size: 20px; }
  .tab.is-active { left: 4px; top: 6px; width: 197px; height: 44px; background: var(--blue); color: var(--white); padding-left: 14px; }
  .tab.is-active strong { font-weight: 600; }
  .tab-updates { left: 206px; width: 186px; border-left: 1px solid var(--panel-border); border-right: 1px solid var(--panel-border); padding-left: 14px; color: var(--text); }
  .tab-updates strong { font-weight: 600; }

  .section-label { position: absolute; left: 24px; top: 91px; font-size: 15px; line-height: 20px; }
  .add-button { position: absolute; left: 874px; top: 83px; }

  .data-table { position: absolute; left: 23px; top: 122px; width: 883px; border-collapse: collapse; font-size: 15px; }
  .data-table th { height: 38px; background: var(--table-head); text-align: left; font-weight: 400; color: var(--text-soft); border-bottom: 2px solid #d4d4d4; }
  .data-table td { height: 46px; color: var(--text-soft); border-bottom: 1px solid var(--row-line); }
  .data-table tr:last-child td { border-bottom: none; }
  .data-table th:first-child, .data-table td:first-child { padding-left: 16px; width: 100px; }
  .data-table .col-date { width: 218px; }
  .data-table .col-title { width: 316px; }
  .data-table .file-link { color: var(--link-red); }
  .time-gap { margin-left: 12px; }

  /* Footer */
  .footer {
    position: absolute; left: 215px; top: 917px; width: 985px; height: 40px; background: var(--white);
    text-align: center; font-size: 12px; line-height: 40px; color: var(--text);
  }
</style>
</head>
<body>
  <header class="topbar">
    <div class="brand">REEF</div>
    <div class="brand-divider"></div>
    <div class="brand-tagline">Call out and support tracker</div>
    <div class="user-menu">Peter Lindqvist<span class="caret"></span></div>
    <div class="help-link">Help</div>
  </header>

  <aside class="sidebar">
    <div class="sidebar-logo">
      <span class="mark"></span>
      <span class="name">VOMIL BRIXTON</span>
    </div>
    <ul class="nav">
      <li class="nav-item">
        <svg width="12" height="12" viewBox="0 0 12 12"><path d="M6 1 0 6h1.5v5h3.5V8h2v3h3.5V6H12z"/></svg>Home</li>
      <li class="nav-item is-active">
        <svg width="13" height="13" viewBox="0 0 13 13"><path d="M1 2.5 2.5 1l10 10-1.5 1.5zM9 1.2l2.8 2.8-2 2-1-1-5 5-1.8-1.8 5-5-1-1z"/></svg>Jobs</li>
      <li class="nav-item">
        <svg width="12" height="12" viewBox="0 0 12 12"><circle cx="6" cy="3.5" r="3"/><path d="M1 12c0-3 2.2-5 5-5s5 2 5 5z"/></svg>Customers</li>
      <li class="nav-item">
        <svg width="13" height="13" viewBox="0 0 13 13"><path d="M3 0h10v11H3zM1 2h1v10h9v1H1z"/></svg>Inventory</li>
      <li class="nav-item">
        <svg width="13" height="13" viewBox="0 0 13 13"><path d="M0 1h2v12H0zM3 5h2v8H3zM6 3h2v10H6zM9 8h2v5H9zM0 12h13v1H0z"/></svg>Reports</li>
      <li class="nav-item">
        <svg width="11" height="13" viewBox="0 0 11 13"><path d="M0 0h7l4 4v9H0zM7 0v4h4"/></svg>Files</li>
      <li class="nav-item">
        <svg width="13" height="11" viewBox="0 0 13 11"><path d="M0 5c0-3 2-5 5-5v2C3.5 2 2.5 3 2.5 5H5v6H0zM8 5c0-3 2-5 5-5v2c-1.5 0-2.5 1-2.5 3H13v6H8z"/></svg>Quotes</li>
    </ul>
  </aside>

  <div class="page-head"><h1>Viewing Job</h1></div>

  <section class="panel panel-personal">
    <div class="panel-title">Personal Information</div>
    <div class="info-row" style="top:50px;height:49px;">
      <div class="field" style="left:0;width:99px;top:14px;"><span class="label">Name</span></div>
      <div class="value" style="left:130px;top:14px;">Martin Hale</div>
      <div class="field" style="left:0;width:540px;top:14px;"><span class="label">Company</span></div>
      <div class="value" style="left:571px;top:14px;">Vomil Brixton Solutions Ltd</div>
    </div>
    <div class="info-row" style="top:99px;height:50px;">
      <div class="field" style="left:0;width:99px;top:11px;"><span class="label">Telephone 1</span></div>
      <div class="value" style="left:130px;top:11px;">07700900417</div>
      <div class="field" style="left:0;width:540px;top:11px;"><span class="label">Email</span></div>
      <div class="value" style="left:571px;top:11px;">martinhale@vomilbrixtonsolutions.co.uk</div>
    </div>
  </section>

  <section class="panel panel-job">
    <div class="panel-title">Job Information</div>
    <div class="info-row" style="top:50px;height:48px;">
      <div class="field" style="left:0;width:99px;top:12px;"><span class="label">Date / Time</span></div>
      <div class="value" style="left:130px;top:12px;">2013-04-17 18:07:02</div>
      <div class="field" style="left:0;width:536px;top:12px;"><span class="label">Job Outstanding?</span></div>
      <div class="value" style="left:571px;top:12px;">Y</div>
    </div>
    <div class="info-row" style="top:98px;height:50px;">
      <div class="field" style="left:0;width:99px;top:11px;"><span class="label">Subject</span></div>
      <div class="value" style="left:130px;top:11px;">Lorem ipsum dolor sit amet, consectetur adipiscing elit</div>
    </div>
    <div class="info-row" style="top:148px;height:100px;">
      <div class="field" style="left:0;width:99px;top:11px;"><span class="label">Description</span></div>
      <div class="value wrap" style="left:130px;top:11px;">Lorem ipsum dolor sit amet, consectetur adipiscing elit. Integer ac neque ligula. Pellentesque bibendum, lorem sit amet pretium ultricies, odio purus faucibus eros, a scelerisque orci leo ac libero. Sed fringilla ultri&shy;cies rutrum. Praesent lacus magna, pharetra eu convallis at, consectetur vitae libero.</div>
    </div>
  </section>

  <section class="panel panel-tabs">
    <div class="tab-bar">
      <div class="tab is-active">
        <svg width="26" height="26" viewBox="0 0 26 26" fill="none" stroke="#ffffff" stroke-width="1.6" stroke-linecap="round"><path d="M18 7 8.5 16.5a2.5 2.5 0 0 0 3.5 3.5L22 10a4.5 4.5 0 0 0-6.4-6.4L5 14.2a6.5 6.5 0 0 0 9.2 9.2L22 15.6"/></svg>
        <span>Attachments <strong>(2)</strong></span>
      </div>
      <div class="tab tab-updates">
        <svg width="32" height="32" viewBox="0 0 32 32"><ellipse cx="14" cy="8" rx="11" ry="4" fill="#c8c8c8" stroke="#8a8a8a"/><path d="M3 8v16c0 2.2 4.9 4 11 4s11-1.8 11-4V8c0 2.2-4.9 4-11 4S3 10.2 3 8z" fill="#b0b0b0" stroke="#8a8a8a"/><path d="M3 14c0 2.2 4.9 4 11 4s11-1.8 11-4M3 19c0 2.2 4.9 4 11 4s11-1.8 11-4" fill="none" stroke="#8a8a8a"/><path d="M22 20h5v5h3l-5.5 6-5.5-6h3z" fill="#1f86d8"/></svg>
        <span>Updates <strong>(1)</strong></span>
      </div>
    </div>
    <div class="section-label">Attachments</div>
    <svg class="add-button" width="28" height="28" viewBox="0 0 28 28"><circle cx="14" cy="14" r="11.5" fill="none" stroke="#2393ec" stroke-width="2.6"/><path d="M14 8v12M8 14h12" stroke="#2393ec" stroke-width="2.8"/></svg>
    <table class="data-table">
      <thead>
        <tr><th>S.no</th><th class="col-date">Date Added</th><th class="col-title">Title</th><th>Filename</th></tr>
      </thead>
      <tbody>
        <tr><td>1</td><td>2014-04-23<span class="time-gap">18:39:49</span></td><td>Pellentesque bibendum</td><td class="file-link">android.png</td></tr>
        <tr><td>1</td><td>2014-04-23<span class="time-gap">18:40:13</span></td><td>Pharetra eu convallis</td><td class="file-link">homenew.png</td></tr>
      </tbody>
    </table>
  </section>

  <footer class="footer">Copyright © 2014 Reef</footer>
</body>
</html>
```